Real Estate Company Needs a Contemporary/Modern Business Card Design

We need a Contemporary/Modern Business Card Design for a New Real Estate Company based in San Francisco, CA called Colvane Terrish Realtors. We would like to see designs that use the color red for the "Colvane Terrish" and gold for the "Realtors." The design should communicate being Modern and yet Established and Stable.

Industry/Entity Type

Business

```html
<!DOCTYPE html>
<html lang="en">
<head>
<meta charset="utf-8">
<title>Colvane Terrish Realtors – Business Card</title>
<link href="https://fonts.googleapis.com/css2?family=Exo+2:wght@400;500;600&display=swap" rel="stylesheet">
<style>
  :root {
    --page: #e9e6e2;
    --card: #ffffff;
    --card-shade: #eeeeee;
    --brand-red: #c0282f;
    --deep-red: #8f1c22;
    --gold: #d9a33a;
    --ink: #3a3a3a;
    --muted: #6a6a6a;
  }
  * { box-sizing: border-box; margin: 0; padding: 0; }
  html, body { width: 1200px; height: 900px; overflow: hidden; }
  body {
    background: var(--page);
    font-family: "Exo 2", sans-serif;
    display: flex;
    align-items: center;
    justify-content: center;
    gap: 40px;
  }
  .card {
    position: relative;
    width: 540px;
    height: 309px;
    background: radial-gradient(ellipse at 40% 35%, var(--card) 40%, var(--card-shade) 100%);
    box-shadow: 0 10px 28px rgba(0,0,0,0.18);
    overflow: hidden;
  }
  .card-wave { position: absolute; inset: 0; width: 100%; height: 100%; }
  .wordmark {
    font-weight: 600;
    color: var(--brand-red);
    letter-spacing: 0.06em;
    text-transform: uppercase;
    display: flex;
    align-items: center;
    gap: 10px;
  }
  .wordmark-square { width: 12px; height: 12px; background: var(--brand-red); flex: none; }
  .card-front .wordmark {
    position: absolute; left: 36px; top: 44px;
    font-size: 17px; line-height: 1.25; width: 210px;
  }
  .contact {
    position: absolute; right: 34px; top: 36px;
    width: 240px;
    font-size: 12.5px; color: var(--ink);
    letter-spacing: 0.03em;
    list-style: none;
  }
  .contact-address { font-size: 13.5px; line-height: 1.35; margin-bottom: 14px; font-weight: 500; }
  .contact li { display: flex; align-items: center; gap: 8px; margin-bottom: 5px; }
  .contact li.contact-address { display: block; }
  .contact svg { width: 12px; height: 12px; flex: none; fill: var(--brand-red); }
  .person {
    position: absolute; left: 36px; bottom: 30px; color: #fff;
  }
  .person-name { font-size: 20px; font-weight: 500; letter-spacing: 0.08em; text-transform: uppercase; }
  .person-title { font-size: 13px; letter-spacing: 0.04em; margin-top: 2px; }
  .card-back { display: flex; align-items: center; justify-content: center; }
  .card-back .wordmark { font-size: 24px; }
</style>
</head>
<body>
  <section class="card card-front" aria-label="Card front">
    <svg class="card-wave" viewBox="0 0 540 309" preserveAspectRatio="none" aria-hidden="true">
      <path d="M0 196 C150 160 300 190 540 232 L540 240 C300 202 150 178 0 214 Z" fill="var(--gold)"/>
      <path d="M0 214 C150 182 310 212 540 246 L540 309 L0 309 Z" fill="var(--brand-red)"/>
      <path d="M0 260 C160 240 330 262 540 296 L540 309 L0 309 Z" fill="var(--deep-red)" opacity="0.35"/>
    </svg>
    <div class="wordmark"><span class="wordmark-square"></span>Colvane Terrish Realtors</div>
    <ul class="contact">
      <li class="contact-address">412 Harlow Street, Suite 9<br>San Francisco</li>
      <li><svg viewBox="0 0 24 24"><path d="M6.6 10.8a15 15 0 0 0 6.6 6.6l2.2-2.2c.3-.3.7-.4 1-.2 1.1.4 2.3.6 3.6.6.6 0 1 .4 1 1V20c0 .6-.4 1-1 1A17 17 0 0 1 3 4c0-.6.4-1 1-1h3.5c.6 0 1 .4 1 1 0 1.3.2 2.5.6 3.6.1.3 0 .7-.2 1z"/></svg>415 555 0182</li>
      <li><svg viewBox="0 0 24 24"><path d="M7 1h10a2 2 0 0 1 2 2v18a2 2 0 0 1-2 2H7a2 2 0 0 1-2-2V3a2 2 0 0 1 2-2zm0 3v14h10V4z"/></svg>415 555 0196</li>
      <li><svg viewBox="0 0 24 24"><path d="M2 5h20v14H2zm2 2v.5l8 5 8-5V7z"/></svg>dorian@colvaneterrish.com</li>
      <li><svg viewBox="0 0 24 24"><path d="M12 2a10 10 0 1 0 0 20 10 10 0 0 0 0-20zm6.9 9h-3a15 15 0 0 0-1.3-5.6A8 8 0 0 1 18.9 11zM12 4c.9 1.2 1.8 3.6 1.9 7h-3.8c.1-3.4 1-5.8 1.9-7zM9.4 5.4A15 15 0 0 0 8.1 11h-3a8 8 0 0 1 4.3-5.6zM5.1 13h3a15 15 0 0 0 1.3 5.6A8 8 0 0 1 5.1 13zM12 20c-.9-1.2-1.8-3.6-1.9-7h3.8c-.1 3.4-1 5.8-1.9 7zm2.6-1.4a15 15 0 0 0 1.3-5.6h3a8 8 0 0 1-4.3 5.6z"/></svg>www.colvaneterrish.com</li>
    </ul>
    <div class="person">
      <p class="person-name">Dorian Maxfield</p>
      <p class="person-title">Managing Director</p>
    </div>
  </section>

  <section class="card card-back" aria-label="Card back">
    <div class="wordmark"><span class="wordmark-square"></span>Colvane Terrish Realtors</div>
  </section>
</body>
</html>
```